need 4 creative A frame (SANDWICH BOARD) designs concepts for dental office

need 4 creative A frame (SANDWICH BOARD) designs concepts
1 - targeting kids
2. targeting old age
3. targeting teens
4 targeting general public

website - www.brenvaxdental.ca

LINK for Measurements for sandwich board https://www.korvepa.ca/BL_1921/Aluminum-Snap-Edge-A-Frame-Sign

i am attaching certain key ingredients ( rough sketch in uploaded files ) to be added on each design though not mandatory if the design is very creative

```html
<!DOCTYPE html>
<html lang="en">
<head>
<meta charset="UTF-8">
<title>Brenvax Dental – A-Frame Sign</title>
<link rel="stylesheet" href="https://fonts.googleapis.com/css2?family=Archivo+Black&family=Open+Sans:wght@400;600&display=swap">
<style>
  :root {
    --stage: #d9d7d6;
    --board-black: #000000;
    --wall-light: #f4f3f1;
    --wall-mid: #e6e3df;
    --sky-blue: #44c1ea;
    --gold-light: #f5da86;
    --gold-dark: #d6a552;
    --logo-grey: #6f7277;
    --ink: #000000;
    --white: #ffffff;
  }
  * { margin: 0; padding: 0; box-sizing: border-box; }
  html, body {
    width: 1200px;
    height: 729px;
    overflow: hidden;
    background: var(--stage);
  }
  .sign-board {
    position: absolute;
    left: 314px;
    top: 0;
    width: 571px;
    height: 729px;
    background: var(--board-black);
    overflow: hidden;
  }
  .hero-photo {
    position: absolute;
    left: 0;
    top: 0;
    width: 571px;
    height: 289px;
    background: linear-gradient(180deg, var(--wall-light) 0%, var(--wall-mid) 55%, #d9b9a9 100%);
  }
  .brand-name {
    position: absolute;
    left: 0;
    top: 28px;
    width: 571px;
    text-align: center;
    font-family: "Archivo Black", sans-serif;
    font-size: 38px;
    line-height: 1;
    color: var(--logo-grey);
  }
  .badge {
    position: absolute;
    top: 272px;
    width: 141px;
    height: 163px;
  }
  .badge svg { position: absolute; left: 0; top: 0; }
  .badge--hours { left: 88px; }
  .badge--billing { left: 344px; }
  .badge-text {
    position: absolute;
    font-family: "Archivo Black", sans-serif;
    color: var(--ink);
    line-height: 1;
  }
  .badge-open { left: 15px; top: 82px; font-size: 16px; }
  .badge-seven { left: 48px; top: 48px; font-size: 84px; }
  .badge-days { left: 81px; top: 99px; font-size: 16px; }
  .badge-billing-text {
    left: 0;
    top: 50px;
    width: 141px;
    text-align: center;
    font-size: 28px;
    line-height: 34px;
  }
  .entry-banner {
    position: absolute;
    left: 120px;
    top: 476px;
    width: 330px;
    height: 60px;
  }
  .entry-banner svg { position: absolute; left: 0; top: 0; }
  .entry-banner-text {
    position: absolute;
    left: 62px;
    top: 0;
    width: 255px;
    text-align: center;
    line-height: 60px;
    font-family: "Archivo Black", sans-serif;
    font-size: 40px;
    color: var(--white);
    letter-spacing: 1px;
  }
  .new-patients {
    position: absolute;
    left: 0;
    top: 576px;
    width: 571px;
    text-align: center;
    font-family: "Open Sans", sans-serif;
    font-weight: 400;
    font-size: 34px;
    color: var(--white);
  }
  .phone-strip {
    position: absolute;
    left: 90px;
    top: 648px;
    width: 396px;
    height: 37px;
    background: var(--sky-blue);
    border-radius: 6px 18px 6px 18px;
  }
  .phone-number {
    position: absolute;
    left: 0;
    top: 0;
    width: 396px;
    text-align: center;
    line-height: 37px;
    font-family: "Open Sans", sans-serif;
    font-weight: 600;
    font-size: 34px;
    color: var(--ink);
  }
</style>
</head>
<body>
  <main class="sign-board">
    <div class="hero-photo" role="img" aria-label="Photo of six young children against a white brick wall, pointing upward"></div>
    <div class="brand-name">Brenvax Dental</div>

    <div class="badge badge--hours">
      <svg width="141" height="163" viewBox="0 0 141 163" aria-hidden="true">
        <defs>
          <linearGradient id="goldHours" x1="0" y1="0" x2="0" y2="1">
            <stop offset="0" stop-color="#f5da86"/>
            <stop offset="1" stop-color="#d6a552"/>
          </linearGradient>
        </defs>
        <path d="M20 0 H121 C116 12,100 20,100 38 L134 75 Q141 83 134 91 L80 157 Q70 167 60 157 L7 91 Q0 83 7 75 L41 38 C41 20,25 12,20 0 Z" fill="url(#goldHours)"/>
        <path d="M20 0 H121 C116 8,106 14,102 22 H39 C35 14,25 8,20 0 Z" fill="#e9c472"/>
      </svg>
      <span class="badge-text badge-open">Open</span>
      <span class="badge-text badge-seven">7</span>
      <span class="badge-text badge-days">Days</span>
    </div>

    <div class="badge badge--billing">
      <svg width="141" height="163" viewBox="0 0 141 163" aria-hidden="true">
        <defs>
          <linearGradient id="goldBilling" x1="0" y1="0" x2="0" y2="1">
            <stop offset="0" stop-color="#f5da86"/>
            <stop offset="1" stop-color="#d6a552"/>
          </linearGradient>
        </defs>
        <path d="M20 0 H121 C116 12,100 20,100 38 L134 75 Q141 83 134 91 L80 157 Q70 167 60 157 L7 91 Q0 83 7 75 L41 38 C41 20,25 12,20 0 Z" fill="url(#goldBilling)"/>
        <path d="M20 0 H121 C116 8,106 14,102 22 H39 C35 14,25 8,20 0 Z" fill="#e9c472"/>
      </svg>
      <div class="badge-text badge-billing-text">We<br>Direct<br>Bill</div>
    </div>

    <div class="entry-banner">
      <svg width="330" height="60" viewBox="0 0 330 60" aria-hidden="true">
        <polygon points="30,0 330,0 330,60 30,60 0,30" fill="#44c1ea"/>
        <polyline points="40,0 11,30 40,60" fill="none" stroke="#000" stroke-width="3"/>
        <polyline points="52,0 23,30 52,60" fill="none" stroke="#000" stroke-width="3"/>
      </svg>
      <div class="entry-banner-text">WE ‘RE IN</div>
    </div>

    <p class="new-patients">Accepting New Patients</p>

    <div class="phone-strip">
      <span class="phone-number">587 555 0148</span>
    </div>
  </main>
</body>
</html>
```